Business Cards for Law Office of Denise R. Harlow

I need a business card for my new estate planning law firm. I have attached my logo. I would like a design that is professional but not too formal or stuffy.

Target Market(s)

Professionals (lawyers, doctors, businesswomen) between the age of 30 and 50 who are tech-savvy and educated.

Industry/Entity Type

Lawyer

Contact Information for Business Card

Denise R. Harlow

528 E. 19th Street
7th Floor
New York, NY 10583

Phone: (855) 602-7318
Direct: (917) 463-5071
Email: Denise@DeniseRHarlowLegal.test
www.DeniseRHarlowLegal.test

Font styles to use
Other font styles liked:
• Corbel

Requirements
Must have
• On the front:
• Denise R. Harlow, Esq.
• Owner & Founder
• 528 E. 19th Street
• 7th Floor
• New York, NY 10583
• Phone: (855) 602-7318
• Direct: (917) 463-5071
• Email: denise@deniserharlowlegal.test
• www.deniserharlowlegal.test
• On the back:
• LOGO
Nice to have
• I want it to be professional but not too formal or stuffy. Please choose colors that go with my logo.
Should not have
• I don't want TOO MUCH color. Some color is good, but not too much.

```html
<!DOCTYPE html>
<html lang="en">
<head>
<meta charset="utf-8">
<title>Business Cards – Law Office of Denise R. Harlow</title>
<link href="https://fonts.googleapis.com/css2?family=Cinzel:wght@400;600&family=Crimson+Text:wght@400;600&display=swap" rel="stylesheet">
<style>
  :root {
    --purple: #7a2a8c;
    --orange: #f0801f;
    --card: #ffffff;
    --backdrop: #3a322e;
  }
  * { box-sizing: border-box; margin: 0; padding: 0; }
  html, body { width: 1200px; height: 900px; overflow: hidden; }
  body {
    background: var(--backdrop);
    position: relative;
    font-family: "Crimson Text", Georgia, serif;
  }
  .card {
    position: absolute;
    width: 560px;
    height: 320px;
    background: var(--card);
    overflow: hidden;
  }

  /* Back: logo side */
  .card-back { left: 60px; top: 100px; }
  .card-back .band-top {
    position: absolute; top: 0; left: 0; right: 0; height: 12px;
    background: var(--purple);
  }
  .card-back .band-bottom {
    position: absolute; bottom: 0; left: 0; right: 0; height: 20px;
    background: var(--orange);
  }
  .firm-name {
    position: absolute; left: 0; right: 0; top: 50%;
    transform: translateY(-55%);
    text-align: center;
    font-family: "Cinzel", "Times New Roman", serif;
    font-weight: 400;
    color: var(--purple);
    font-size: 30px;
    line-height: 1.25;
    letter-spacing: 1px;
  }

  /* Front: contact side */
  .card-front { left: 580px; top: 480px; }
  .card-front .band-bottom {
    position: absolute; bottom: 0; left: 0; right: 0; height: 14px;
    display: flex;
  }
  .band-bottom .seg-orange { width: 45%; background: var(--orange); }
  .band-bottom .seg-purple { flex: 1; background: var(--purple); }

  .identity {
    position: absolute; left: 40px; top: 92px; width: 235px;
    text-align: right;
  }
  .person-name {
    font-family: "Cinzel", "Times New Roman", serif;
    font-weight: 600;
    color: var(--purple);
    font-size: 17px;
    letter-spacing: 0.5px;
    white-space: nowrap;
  }
  .person-title {
    font-family: "Cinzel", "Times New Roman", serif;
    color: var(--orange);
    font-size: 12px;
    letter-spacing: 1px;
    margin-top: 2px;
  }
  .divider {
    position: absolute; left: 296px; top: 80px;
    width: 1px; height: 120px; background: var(--purple);
  }
  .contact-list {
    position: absolute; left: 312px; top: 86px;
    list-style: none;
  }
  .contact-list li {
    display: flex; align-items: center; gap: 9px;
    color: var(--purple);
    font-size: 15px;
    line-height: 27px;
    white-space: nowrap;
  }
  .icon {
    width: 15px; height: 15px; flex: none;
    background: var(--orange); border-radius: 2px;
    display: flex; align-items: center; justify-content: center;
  }
  .icon svg { width: 10px; height: 10px; }
  .address {
    position: absolute; left: 40px; bottom: 46px;
    color: var(--purple);
    font-size: 15px;
    letter-spacing: 0.2px;
  }
</style>
</head>
<body>

  <section class="card card-back" aria-label="Card back with firm name">
    <div class="band-top"></div>
    <p class="firm-name">Law Office of<br>Denise R. Harlow</p>
    <div class="band-bottom"></div>
  </section>

  <section class="card card-front" aria-label="Card front with contact details">
    <div class="identity">
      <p class="person-name">Denise R. Harlow, Esq.</p>
      <p class="person-title">Owner &amp; Founder</p>
    </div>
    <div class="divider"></div>
    <ul class="contact-list">
      <li><span class="icon"><svg viewBox="0 0 10 10"><path d="M2 1 L4 1 L4.6 3 L3.5 3.8 Q4.4 5.7 6.2 6.5 L7 5.4 L9 6 L9 8 Q5 9 2.2 5.5 Q1 3.5 2 1 Z" fill="#fff"/></svg></span>(855) 602-7318</li>
      <li><span class="icon"><svg viewBox="0 0 10 10"><path d="M2 1 L4 1 L4.6 3 L3.5 3.8 Q4.4 5.7 6.2 6.5 L7 5.4 L9 6 L9 8 Q5 9 2.2 5.5 Q1 3.5 2 1 Z" fill="#fff"/></svg></span>Direct: (917) 463-5071</li>
      <li><span class="icon"><svg viewBox="0 0 10 10"><rect x="1" y="2.2" width="8" height="5.6" fill="none" stroke="#fff" stroke-width="1"/><path d="M1 2.4 L5 5.6 L9 2.4" fill="none" stroke="#fff" stroke-width="1"/></svg></span>denise@deniserharlowlegal.test</li>
      <li><span class="icon"><svg viewBox="0 0 10 10"><circle cx="5" cy="5" r="3.8" fill="none" stroke="#fff" stroke-width="0.9"/><ellipse cx="5" cy="5" rx="1.6" ry="3.8" fill="none" stroke="#fff" stroke-width="0.8"/><path d="M1.2 5 H8.8" stroke="#fff" stroke-width="0.8"/></svg></span>www.deniserharlowlegal.test</li>
    </ul>
    <p class="address">528 E. 19th Street, 7th Floor, New York, NY 10583</p>
    <div class="band-bottom"><span class="seg-orange"></span><span class="seg-purple"></span></div>
  </section>

</body>
</html>
```